Curantel System Web Page Design

This project is to design 6 pages of a web based medical system for clinics, hospitals, drugs suppliers, general items suppliers, insurance company, laboratories and patients (basically all parties which could be involved in).We want the designs of the browser, button, icon and layout are based on Oru, which is user friendly, looks professional, simple and neat but with powerful functions. We have uploaded few pictures of another system, please do not copy its design because this is not what we are looking for, the pictures are for you to know the elements should be included in our pages. Curantel web-base system, design 6 pages1. Login PageShould include the following elements-company id with input field-login id with input field-password with input field2. Main Page (Navigation page)Should include the following elements-Appointment-Consultation-Patient-Drugs inventory -General supplies inventory -Laboratory-Suppliers-Insurance-Reports 3. Appointment PageShould include all the the elements in the respective pictures plus the followings-Daily View, Weekly View, Monthly View buttons4. Consultation PageShould include all the the elements in the respective picture5. Patient Page5.1 General information Should include all the the elements in the respective picture5.2 medical history/lab reportsShould include all the the elements in the respective picture plus the followings-Notify patient button-Share report button.
Please stop using Ward Harbor in your designs which is not the name of our system. We have just rename our system to Curantel, please take note.
We need the system to look professional not playful, do not use too many colors and playful icons.
professional users
5+ page

```html
<!DOCTYPE html>
<html lang="en">
<head>
<meta charset="utf-8">
<title>Curantel System</title>
<link href="https://fonts.googleapis.com/css2?family=Arimo:wght@400;700&display=swap" rel="stylesheet">
<style>
  :root {
    --page-bg: #e2e2e2;
    --frame-border: #9a9a9a;
    --titlebar-top: #f1f1f1;
    --titlebar-bottom: #dcdcdc;
    --title-text: #3a3a3a;
    --workspace-top: #2a7cc4;
    --workspace-bottom: #1f6cb3;
    --tile-top: #e3f2fc;
    --tile-mid: #c6e5f8;
    --tile-bottom: #a4d6f3;
    --tile-active: #ffffff;
    --icon-stroke: #1f5f9e;
    --label-text: #ffffff;
    --close: #fc5f57;
    --minimize: #fdbc2e;
    --zoom: #33c748;
  }
  * { box-sizing: border-box; margin: 0; padding: 0; }
  html, body {
    width: 1200px; height: 761px; overflow: hidden;
    background: var(--page-bg);
    font-family: "Arimo", "Helvetica Neue", Arial, sans-serif;
  }
  .app-window {
    position: absolute; left: 37px; top: 60px; width: 1128px; height: 641px;
    border: 1px solid var(--frame-border); border-radius: 6px; overflow: hidden;
    box-shadow: 0 18px 30px rgba(0,0,0,0.28);
    background: linear-gradient(var(--workspace-top), var(--workspace-bottom));
  }
  .title-bar {
    height: 31px; position: relative;
    background: linear-gradient(var(--titlebar-top), var(--titlebar-bottom));
    border-bottom: 1px solid #b5b5b5;
  }
  .window-controls { position: absolute; left: 11px; top: 9px; display: flex; gap: 8px; }
  .window-controls span { width: 13px; height: 13px; border-radius: 50%; border: 1px solid rgba(0,0,0,0.2); }
  .control-close { background: var(--close); }
  .control-minimize { background: var(--minimize); }
  .control-zoom { background: var(--zoom); }
  .window-title {
    text-align: center; line-height: 31px; font-size: 16px; color: var(--title-text);
  }
  .fullscreen-toggle { position: absolute; right: 8px; top: 8px; }
  .welcome-heading {
    position: absolute; top: 96px; width: 100%; text-align: center;
    color: var(--label-text); font-weight: 400; font-size: 25px;
  }
  .module {
    position: absolute; width: 177px; text-align: center; color: var(--label-text);
    text-decoration: none; font-size: 19px; line-height: 1.3;
  }
  .module-tile {
    height: 110px; display: flex; align-items: center; justify-content: center;
    background: linear-gradient(var(--tile-top) 0%, var(--tile-mid) 55%, var(--tile-bottom) 100%);
    box-shadow: 0 1px 2px rgba(0,0,0,0.2);
  }
  .module-tile svg { width: 72px; height: 72px; fill: none; stroke: var(--icon-stroke); stroke-width: 2.4; stroke-linecap: round; stroke-linejoin: round; }
  .module-label { display: block; margin-top: 10px; }
  .module.is-active .module-tile { background: var(--tile-active); }
  .module.is-active .module-label { font-weight: 700; }
  .pointer { position: absolute; left: 445px; top: 314px; }
</style>
</head>
<body>
<div class="app-window">
  <div class="title-bar">
    <div class="window-controls"><span class="control-close"></span><span class="control-minimize"></span><span class="control-zoom"></span></div>
    <div class="window-title">Curantel System</div>
    <svg class="fullscreen-toggle" width="16" height="16" viewBox="0 0 16 16"><path d="M9 2h5v5M14 2 9 7M7 14H2V9M2 14l5-5" stroke="#8a8a8a" stroke-width="1.6" fill="none"/></svg>
  </div>

  <h1 class="welcome-heading">Welcome to Curantel System</h1>

  <a class="module" style="left:43px;top:184px" href="#">
    <div class="module-tile"><svg viewBox="0 0 72 72"><circle cx="30" cy="20" r="10"/><path d="M10 58v-8a14 14 0 0 1 14-14h10"/><path d="M10 58h30"/><circle cx="48" cy="48" r="12"/><path d="M48 41v7l5 4"/></svg></div>
    <span class="module-label">Appointment</span>
  </a>
  <a class="module is-active" style="left:260px;top:184px" href="#">
    <div class="module-tile"><svg viewBox="0 0 72 72"><rect x="24" y="10" width="24" height="12"/><rect x="28" y="14" width="16" height="4"/><circle cx="14" cy="22" r="5"/><circle cx="58" cy="22" r="5"/><path d="M8 50V34a6 6 0 0 1 12 0v10h8M64 50V34a6 6 0 0 0-12 0v10h-8"/><path d="M18 32h36M36 32v24M26 56h20M14 50v10M58 50v10"/></svg></div>
    <span class="module-label">Consultation</span>
  </a>
  <a class="module" style="left:475px;top:184px" href="#">
    <div class="module-tile"><svg viewBox="0 0 72 72"><circle cx="36" cy="16" r="9"/><path d="M22 62V38a12 12 0 0 1 12-12h4a12 12 0 0 1 12 12v24"/><path d="M22 40l12 10-4 6"/></svg></div>
    <span class="module-label">Patient</span>
  </a>
  <a class="module" style="left:692px;top:184px" href="#">
    <div class="module-tile"><svg viewBox="0 0 72 72"><rect x="18" y="6" width="36" height="60" rx="3"/><path d="M18 14h36M24 22h24"/><rect x="28" y="30" width="8" height="16" rx="4"/><circle cx="44" cy="42" r="6"/><path d="M40 46l8-8"/><circle cx="26" cy="56" r="1.5"/><circle cx="36" cy="56" r="1.5"/><circle cx="46" cy="56" r="1.5"/></svg></div>
    <span class="module-label">Drugs Inventory</span>
  </a>
  <a class="module" style="left:907px;top:184px" href="#">
    <div class="module-tile"><svg viewBox="0 0 72 72"><rect x="10" y="14" width="44" height="46"/><path d="M18 26h24M18 34h20M18 42h14M18 50h10"/><path d="M60 10l4 4-22 22-6 2 2-6z"/></svg></div>
    <span class="module-label">General Supplies Inventory</span>
  </a>

  <a class="module" style="left:150px;top:398px" href="#">
    <div class="module-tile"><svg viewBox="0 0 72 72"><path d="M26 12v18L12 58a4 4 0 0 0 4 6h24a4 4 0 0 0 4-6L30 30V12"/><path d="M22 12h12M16 50h32"/><path d="M48 10h14M52 10v48a3 3 0 0 0 6 0V10"/><path d="M52 34h6"/><path d="M34 8h12v30"/></svg></div>
    <span class="module-label">Laboratory</span>
  </a>
  <a class="module" style="left:367px;top:398px" href="#">
    <div class="module-tile"><svg viewBox="0 0 72 72"><circle cx="24" cy="12" r="5"/><path d="M16 40V24a4 4 0 0 1 4-4h8a4 4 0 0 1 4 4v16"/><path d="M19 40v22M29 40v22"/><path d="M38 36h6v24h14"/><circle cx="44" cy="62" r="3"/></svg></div>
    <span class="module-label">Suppliers</span>
  </a>
  <a class="module" style="left:582px;top:398px" href="#">
    <div class="module-tile"><svg viewBox="0 0 72 72"><path d="M8 36a28 24 0 0 1 56 0c-4-4-10-4-14 0-4-4-10-4-14 0-4-4-10-4-14 0-4-4-10-4-14 0z"/><path d="M36 12v46a5 5 0 0 1-10 0"/><path d="M36 12C28 18 24 26 22 36M36 12c8 6 12 14 14 24"/></svg></div>
    <span class="module-label">Insurance</span>
  </a>
  <a class="module" style="left:799px;top:398px" href="#">
    <div class="module-tile"><svg viewBox="0 0 72 72"><rect x="14" y="10" width="44" height="56" rx="2"/><rect x="28" y="6" width="16" height="8"/><path d="M22 24h28M22 32h28M22 40h28M22 48h20M22 56h14"/></svg></div>
    <span class="module-label">Reports</span>
  </a>

  <svg class="pointer" width="16" height="24" viewBox="0 0 16 24"><path d="M1 1v19l5-5 4 8 3-1-4-8h7z" fill="#000" stroke="#fff" stroke-width="1"/></svg>
</div>
</body>
</html>
```